Brantwell Group needs a business card design

We need a new business card design using the logo recently selected in a logo competition on Pixel Forum. Our business is a consultancy specializing in aviation and energy and the winning business card design will promote an image of precision and professionalism with creativity.

Please use the logo with the name on the front of the card and use a complementary font. Make the back white with either the light grey or dark grey logo.

Target Market(s)

Senior finance and legal leaders at aviation and energy companies

Industry/Entity Type

Management Consulting

Contact Information for Business Card

Peter Haldane
President
Brantwell Group

www.brantwellgroup.example

(555) 304-6198
ph@brantwellgroup.example

Requirements
Must have
• Professional font that goes well with the logo font

```html
<!DOCTYPE html>
<html lang="en">
<head>
<meta charset="utf-8">
<title>Brantwell Group – Business Card</title>
<link rel="stylesheet" href="https://fonts.googleapis.com/css2?family=PT+Sans+Narrow&family=Questrial&display=swap">
<style>
  :root {
    --navy: #173f70;
    --white: #ffffff;
    --paper-light: #f3f4f8;
    --grey: #666666;
    --grey-text: #555555;
    --backdrop-top: #2a2a2a;
    --backdrop-bottom: #050505;
  }
  html, body {
    margin: 0;
    padding: 0;
    width: 1200px;
    height: 900px;
    overflow: hidden;
  }
  .stage {
    position: relative;
    width: 1200px;
    height: 900px;
    background: linear-gradient(180deg, var(--backdrop-top) 0%, #161616 55%, var(--backdrop-bottom) 100%);
  }
  .card {
    position: absolute;
    top: 170px;
    width: 346px;
    height: 560px;
    overflow: hidden;
    box-shadow: 0 2px 6px rgba(0,0,0,0.5);
  }
  .card--front { left: 259px; background: var(--white); }
  .card--back { left: 631px; background: var(--paper-light); }

  .front-shapes { position: absolute; inset: 0; }

  .holder {
    position: absolute;
    top: 40px;
    width: 100%;
    text-align: center;
    color: var(--white);
    font-family: "PT Sans Narrow", "Arial Narrow", sans-serif;
  }
  .holder__name { font-size: 29px; line-height: 1; letter-spacing: 0.2px; }
  .holder__title { font-size: 16px; margin-top: 5px; }

  .brand-square {
    position: absolute;
    background: var(--navy);
  }
  .card--front .brand-square { top: 142px; left: 151px; width: 44px; height: 44px; }

  .wordmark {
    position: absolute;
    left: 0;
    width: 100%;
    text-align: center;
    font-family: "Questrial", "Helvetica Neue", sans-serif;
    font-weight: 400;
  }
  .card--front .wordmark { top: 219px; color: var(--navy); }
  .wordmark__name { font-size: 27px; letter-spacing: 2px; line-height: 1; }
  .wordmark__sub { font-size: 13px; letter-spacing: 11px; margin-top: 8px; padding-left: 11px; }
  .card--front .wordmark__sub { color: var(--grey-text); }

  .contact {
    position: absolute;
    top: 480px;
    width: 100%;
    text-align: center;
    color: var(--white);
    font-family: "PT Sans Narrow", "Arial Narrow", sans-serif;
    font-size: 16px;
    line-height: 21px;
  }
  .contact__line { display: flex; align-items: center; justify-content: center; gap: 5px; }
  .contact__icon { width: 11px; height: 11px; }

  .card--back .brand-square { top: 190px; left: 88px; width: 170px; height: 170px; background: var(--grey); }

  .back-band {
    position: absolute;
    left: 0;
    bottom: 0;
    width: 100%;
    height: 132px;
    background: var(--grey);
  }
  .card--back .wordmark { top: 46px; color: var(--white); }
  .card--back .wordmark__name { font-size: 40px; letter-spacing: 2px; }
  .card--back .wordmark__sub { font-size: 19px; letter-spacing: 21px; padding-left: 21px; margin-top: 12px; }
</style>
</head>
<body>
<main class="stage">
  <section class="card card--front">
    <svg class="front-shapes" width="346" height="560" viewBox="0 0 346 560" aria-hidden="true">
      <rect x="0" y="0" width="346" height="126" fill="var(--navy)"/>
      <rect x="54" y="121" width="226" height="5" fill="var(--white)"/>
      <polygon points="173,308 346,460 346,560 0,560 0,460" fill="var(--navy)"/>
    </svg>
    <div class="holder">
      <div class="holder__name">PETER HALDANE</div>
      <div class="holder__title">President</div>
    </div>
    <div class="brand-square" role="img" aria-label="Brantwell Group brand mark"></div>
    <div class="wordmark">
      <div class="wordmark__name">BRANTWELL</div>
      <div class="wordmark__sub">GROUP</div>
    </div>
    <div class="contact">
      <div class="contact__line">
        <svg class="contact__icon" viewBox="0 0 12 12" aria-hidden="true"><path d="M1 4 Q6 0 11 4 L9 5.5 L8 4 L4 4 L3 5.5 Z M3 6 L9 6 L10 11 L2 11 Z" fill="var(--white)"/></svg>
        <span>(555) 304-6198</span>
      </div>
      <div class="contact__line">
        <svg class="contact__icon" viewBox="0 0 12 12" aria-hidden="true"><rect x="0.5" y="2" width="11" height="8" fill="var(--white)"/><path d="M1 2.5 L6 6.5 L11 2.5" stroke="var(--navy)" stroke-width="1" fill="none"/></svg>
        <span>ph@brantwellgroup.example</span>
      </div>
    </div>
  </section>

  <section class="card card--back">
    <div class="brand-square" role="img" aria-label="Brantwell Group brand mark, large"></div>
    <div class="back-band">
      <div class="wordmark">
        <div class="wordmark__name">BRANTWELL</div>
        <div class="wordmark__sub">GROUP</div>
      </div>
    </div>
  </section>
</main>
</body>
</html>
```